Agency Website & Personal brand

My name is Petros Valtinos & I've been a digital marketer & an e-commerce expert since 2010.

- I've spoken to 20 different events around the world up to 3,000 people in size.
- I've sold over 1500 training courses around e-commerce growth.
- I have over 100 testimonials (video & photo) from successful students who bought my training
- I have dozens of video testimonials from respected entrepreneurs that vouch for me and my work
- I have photos with marketing legends with that I shared the stage like Owen Farrow, Thomas Brennigan, Colin Marsh & more
- I am the host of the Aegean Roundtable since 2017 - a high-level networking event for 7 & 8 figure entrepreneurs - 100 people have come to Greece since 2017
- I have tons of videos created where I showcase my expertise on growth
- I have worked with dozens of e-commerce stores on their growth & helped them scale to multiple 6, 7 & 8 figures either on consulting

I need a website design that showcases my authority & be a lead generating machine.

The goal is to bring people on a call with me but also grab their email and start building the relationship with them and free valuable content

We have 3 offers :

1. Paid ads (Done for You)
2. Consulting/Mastermind (Done with You)
3. Training (Do it Yourself)

```html
<!DOCTYPE html>
<html lang="en">
<head>
<meta charset="utf-8">
<title>Petros Valtinos – Public Speaker &amp; eCom Trainer</title>
<link rel="stylesheet" href="https://fonts.googleapis.com/css2?family=Poppins:wght@400;500;600;700;800&display=swap">
<style>
  :root {
    --red: #dc1f41;
    --dark: #1d1d1f;
    --dark-2: #2a2a2d;
    --light: #f1f1f1;
    --text: #333;
    --muted: #555;
    --white: #fff;
  }
  * { box-sizing: border-box; margin: 0; padding: 0; }
  html, body { width: 1200px; height: 4246px; overflow: hidden; }
  body { font-family: "Poppins", sans-serif; color: var(--text); background: var(--white); }
  .page { position: relative; width: 1200px; height: 4246px; overflow: hidden; }
  .abs { position: absolute; }
  .btn { position: absolute; background: var(--red); color: var(--white); font-weight: 600; font-size: 14px; text-transform: uppercase; display: flex; align-items: center; justify-content: center; letter-spacing: .2px; }

  /* Hero */
  .hero-bg { position: absolute; left: 0; top: 0; width: 1200px; height: 690px;
    background: linear-gradient(115deg, #6b63c8 0%, #8c8fd6 35%, #a9c1e6 60%, #b8cde8 80%, #8fa6cf 100%); }
  .hero-speaker { position: absolute; left: 560px; top: 40px; width: 330px; height: 600px;
    background: linear-gradient(180deg, #5a5f73 0%, #3c4256 60%, #2c3142 100%); border-radius: 150px 150px 0 0; opacity: .85; }
  .brand { left: 99px; top: 22px; font-size: 29px; color: var(--white); font-weight: 400; }
  .nav { left: 474px; top: 30px; display: flex; gap: 42px; font-size: 14px; color: var(--white); }
  .nav-contact { left: 960px; top: 22px; width: 140px; height: 36px; font-size: 14px; }
  .hero-title { left: 99px; top: 168px; width: 460px; font-size: 50px; line-height: 50px; font-weight: 600; color: var(--white); }
  .hero-sub { left: 99px; top: 337px; width: 420px; font-size: 21px; line-height: 29px; color: var(--white); }
  .hero-cta { left: 99px; top: 406px; font-size: 18px; color: var(--white); }
  .hero-cta span { border-bottom: 1px solid var(--white); }
  .hero-input { left: 99px; top: 460px; width: 403px; height: 35px; background: var(--white); font-size: 12px; color: #444; padding: 10px 12px; }
  .hero-btn { left: 99px; top: 506px; width: 403px; height: 36px; font-size: 14px; }

  /* About */
  .video-frame { left: 120px; top: 750px; width: 485px; height: 370px; background: var(--white); box-shadow: 0 2px 12px rgba(0,0,0,.25); }
  .video-still { position: absolute; left: 8px; top: 8px; width: 469px; height: 354px; background: linear-gradient(160deg, #e9e9ea 0%, #c9c9cc 50%, #5a5e6a 100%); }
  .play-red { position: absolute; left: 208px; top: 150px; width: 56px; height: 56px; border-radius: 50%; background: var(--red); }
  .about-title { left: 664px; top: 768px; font-size: 34px; font-weight: 600; color: #111; }
  .about-text { left: 666px; top: 820px; width: 420px; font-size: 15.5px; line-height: 31px; color: var(--muted); }
  .about-btn { left: 666px; top: 1060px; width: 142px; height: 36px; }

  /* Story */
  .story-bg { left: 0; top: 1203px; width: 1200px; height: 667px; background: var(--dark); }
  .ghost { position: absolute; font-weight: 800; color: rgba(255,255,255,.06); letter-spacing: 4px; }
  .story-title { left: 98px; top: 1337px; font-size: 34px; font-weight: 600; color: var(--white); }
  .story-list { left: 98px; top: 1402px; width: 470px; list-style: none; color: var(--white); font-size: 15.5px; line-height: 21px; }
  .story-list li { position: relative; padding-left: 20px; margin-bottom: 14px; }
  .story-list li::before { content: ""; position: absolute; left: 0; top: 5px; width: 11px; height: 11px; border: 1.5px solid var(--white); border-radius: 50%; }
  .story-list li::after { content: ""; position: absolute; left: 4px; top: 9px; width: 5px; height: 5px; background: var(--white); border-radius: 50%; }
  .story-btn { left: 100px; top: 1709px; width: 142px; height: 35px; }
  .story-name { left: 620px; top: 1335px; font-size: 104px; line-height: 106px; font-weight: 700; color: var(--white); letter-spacing: -1px; }
  .story-portrait { left: 640px; top: 1255px; width: 480px; height: 580px; background: linear-gradient(180deg, #3b4a66 0%, #2f5f93 55%, #24467a 100%); border-radius: 220px 220px 0 0; opacity: .92; }

  /* Offer */
  .offer-bg { left: 0; top: 1870px; width: 1200px; height: 540px; background: var(--light); }
  .section-title { position: absolute; width: 1200px; left: 0; text-align: center; font-size: 33px; font-weight: 600; }
  .offer { position: absolute; top: 2003px; width: 300px; text-align: center; }
  .offer-icon { width: 126px; height: 126px; margin: 0 auto; border-radius: 50%; background: var(--dark-2); border: 4px solid var(--red); display: flex; align-items: center; justify-content: center; }
  .offer h3 { margin-top: 14px; font-size: 21px; font-weight: 500; color: #111; }
  .offer p { margin-top: 10px; font-size: 13.5px; line-height: 28px; color: var(--muted); }
  .offer a { display: inline-block; margin-top: 10px; font-size: 15px; font-weight: 500; color: var(--red); text-decoration: underline; }

  /* Testimonials */
  .testi-bg { left: 0; top: 2409px; width: 1200px; height: 681px; background: var(--dark); }
  .testi-video { left: 99px; top: 2591px; width: 494px; height: 342px; border-radius: 10px; background: linear-gradient(160deg, #5c3fd0 0%, #2e2a7a 40%, #262430 100%); box-shadow: 6px 6px 0 var(--red); }
  .play-ring { position: absolute; left: 218px; top: 142px; width: 58px; height: 58px; border-radius: 50%; border: 3px solid var(--white); }
  .dots { left: 296px; top: 2953px; display: flex; gap: 14px; align-items: center; }
  .dots span { width: 11px; height: 11px; border-radius: 50%; background: var(--white); }
  .dots span:first-child { width: 20px; height: 20px; border: 3px solid var(--white); background: var(--dark); box-shadow: inset 0 0 0 3px var(--dark), inset 0 0 0 10px var(--white); }
  .review { position: absolute; left: 660px; width: 440px; }
  .avatar { position: absolute; left: 0; top: 0; width: 88px; height: 88px; border-radius: 50%; background: linear-gradient(160deg, #dfe3e8, #9aa3ad); border: 3px solid var(--white); }
  .quote { position: absolute; left: 24px; top: 74px; }
  .review-body { margin-left: 109px; color: var(--white); }
  .review-name { font-size: 14px; font-weight: 600; }
  .review-name small { font-weight: 400; font-size: 12px; margin-left: 6px; padding-left: 8px; border-left: 1px solid var(--white); }
  .review-text { margin-top: 6px; font-size: 13.5px; line-height: 25px; }

  /* Gallery */
  .gallery { left: 100px; top: 3207px; width: 1000px; display: grid; grid-template-columns: repeat(4, 238px); grid-auto-rows: 230px; column-gap: 16px; row-gap: 19px; }
  .gallery div { border: 1px solid #ddd; }
  .gallery-btn { left: 530px; top: 3718px; width: 141px; height: 36px; }

  /* Footer */
  .footer-bg { left: 0; top: 3860px; width: 1200px; height: 386px; background: var(--dark); }
  .newsletter { left: 99px; top: 3827px; width: 1002px; height: 92px; background: var(--white); box-shadow: 12px -12px 0 #9a9a9c; }
  .newsletter h2 { position: absolute; left: 30px; top: 24px; font-size: 33px; font-weight: 600; color: #111; }
  .nl-input { position: absolute; left: 376px; top: 26px; width: 436px; height: 40px; background: #f1f1f1; font-size: 12px; padding: 12px 14px; color: #444; }
  .nl-btn { left: 828px; top: 26px; width: 142px; height: 40px; }
  .footer-brand { left: 0; width: 1200px; top: 3970px; text-align: center; font-size: 38px; color: var(--white); font-weight: 400; }
  .socials { left: 514px; top: 4036px; display: flex; gap: 6px; }
  .socials span { width: 38px; height: 38px; border-radius: 50%; border: 1.5px solid var(--white); display: flex; align-items: center; justify-content: center; color: var(--white); font-size: 13px; font-weight: 500; }
  .footer-nav { left: 208px; top: 4108px; display: flex; font-size: 15px; color: var(--white); }
  .footer-nav span { padding: 0 40px; border-left: 1px solid var(--white); line-height: 18px; }
  .footer-nav span:first-child { border-left: 0; padding-left: 0; }
  .footer-rule { left: 100px; top: 4172px; width: 1000px; height: 1px; background: #3a3a3c; }
  .copyright { left: 0; width: 1200px; top: 4196px; text-align: center; font-size: 15px; color: var(--white); }
</style>
</head>
<body>
<div class="page">

  <!-- Hero -->
  <div class="hero-bg" role="img" aria-label="Photo of the speaker on stage at a summit, wearing a blazer and headset microphone"></div>
  <div class="hero-speaker" role="img" aria-label="Speaker standing on stage"></div>
  <svg class="abs" style="left:0;top:570px" width="1200" height="130" viewBox="0 0 1200 130">
    <polygon points="0,106 560,52 1200,8 1200,120 0,130" fill="#dc1f41"/>
    <polygon points="0,106 1200,28 1200,130 0,130" fill="#fff"/>
  </svg>
  <div class="abs brand">Petros Valtinos</div>
  <nav class="abs nav"><span>HOME</span><span>ABOUT US</span><span>OUR SERVICES</span><span>TESTIMONIALS</span></nav>
  <div class="btn nav-contact">Contact Me</div>
  <h1 class="abs hero-title">Public Speaker &amp; Trainer, eCom expert</h1>
  <p class="abs hero-sub">Building &amp; Scaling ecom brands before it was cool (est 2010)</p>
  <p class="abs hero-cta">Book A Free Strategy <span>Call Now!</span></p>
  <div class="abs hero-input">Enter Email Here</div>
  <div class="btn hero-btn">Sign Up For My Free Training</div>

  <!-- About -->
  <div class="abs video-frame">
    <div class="video-still" role="img" aria-label="Video still of two men seated in an interview with a camera between them">
      <div class="play-red"></div>
      <svg class="abs" style="left:229px;top:167px" width="20" height="22" viewBox="0 0 20 22"><polygon points="2,1 19,11 2,21" fill="#fff"/></svg>
    </div>
  </div>
  <h2 class="abs about-title">Hi i’m Petros Valtinos</h2>
  <p class="abs about-text">Lorem ipsum dolor sit amet, consetur adipiscing elit, sed do eiusmod tempor incididure et dolore magna aliqua. Quis ipsum suspendisse ultces gravida. Risus commodo viverra maecenas acan lacus vel facilisis. Lorem ipsum dolor sit amet, consetur adipiscing elit, sed do eiusmod tempor incididure et dolore magna aliqua. Quis ipsum suspendisse ultces gravida.</p>
  <div class="btn about-btn">Learn More</div>

  <!-- Story -->
  <div class="abs story-bg"></div>
  <svg class="abs" style="left:0;top:1200px" width="1200" height="60" viewBox="0 0 1200 60">
    <polygon points="0,0 640,28 0,56" fill="#dc1f41"/>
    <polygon points="0,0 1200,0 1200,3 640,28" fill="#fff"/>
  </svg>
  <div class="ghost" style="left:94px;top:1270px;font-size:92px">STORY</div>
  <div class="abs story-name">PETROS<br>VALTINOS</div>
  <div class="abs story-portrait" role="img" aria-label="Portrait of the speaker in a blue blazer with a conference lanyard and headset"></div>
  <h2 class="abs story-title">My Story</h2>
  <ul class="abs story-list">
    <li>I've spoken to 20 different events around the world up to 3,000 people in size.</li>
    <li>I've sold over 1500 training courses around e-commerce growth.</li>
    <li>I have over 100 testimonials (video &amp; photo) from successful students who bought my training</li>
    <li>I have dozens of video testimonials from respected entrepreneurs that vouch for me and my work</li>
    <li>I have photos with marketing legends with that I shared the stage like Owen Farrow, Thomas Brennigan, Colin Marsh &amp; more</li>
  </ul>
  <div class="btn story-btn">Learn More</div>
  <svg class="abs" style="left:0;top:1815px" width="1200" height="56" viewBox="0 0 1200 56">
    <polygon points="560,56 1200,0 1200,56" fill="#dc1f41"/>
  </svg>

  <!-- Offer -->
  <div class="abs offer-bg"></div>
  <h2 class="section-title" style="top:1918px;color:#111">What We Offer</h2>
  <div class="offer" style="left:100px">
    <div class="offer-icon">
      <svg width="60" height="60" viewBox="0 0 60 60" fill="none" stroke="#fff" stroke-width="2.5"><rect x="10" y="14" width="40" height="32" rx="3"/><line x1="10" y1="22" x2="50" y2="22"/><polyline points="16,40 24,32 31,37 43,27"/><circle cx="14" cy="12" r="6"/></svg>
    </div>
    <h3>Paid ads</h3>
    <p>Lorem ipsum dolor sit amet, kltur adipiscing elit, sed do eiusmod tempor iidure et dolore magna aliqua. Quis ipm suspendisse ultces gravida. Risus commodo</p>
    <a>LEARN MORE</a>
  </div>
  <div class="offer" style="left:450px">
    <div class="offer-icon">
      <svg width="60" height="60" viewBox="0 0 60 60" fill="none" stroke="#fff" stroke-width="2.5"><rect x="20" y="10" width="20" height="12" rx="2"/><circle cx="12" cy="22" r="4"/><circle cx="48" cy="22" r="4"/><path d="M6 46v-12h10v12M44 46v-12h10v12"/><line x1="18" y1="32" x2="42" y2="32"/><line x1="30" y1="32" x2="30" y2="48"/></svg>
    </div>
    <h3>Consulting</h3>
    <p>Lorem ipsum dolor sit amet, kltur adipiscing elit, sed do eiusmod tempor iidure et dolore magna aliqua. Quis ipm suspendisse ultces gravida. Risus commodo</p>
    <a>LEARN MORE</a>
  </div>
  <div class="offer" style="left:799px">
    <div class="offer-icon">
      <svg width="60" height="60" viewBox="0 0 60 60" fill="none" stroke="#fff" stroke-width="2.5"><rect x="22" y="10" width="30" height="22" rx="2"/><line x1="27" y1="18" x2="46" y2="18"/><line x1="27" y1="24" x2="40" y2="24"/><circle cx="14" cy="22" r="5"/><path d="M8 50v-16h12l10-6M14 34v16"/></svg>
    </div>
    <h3>Training</h3>
    <p>Lorem ipsum dolor sit amet, kltur adipiscing elit, sed do eiusmod tempor iidure et dolore magna aliqua. Quis ipm suspendisse ultces gravida. Risus commodo</p>
    <a>LEARN MORE</a>
  </div>

  <!-- Testimonials -->
  <div class="abs testi-bg"></div>
  <svg class="abs" style="left:0;top:2406px" width="1200" height="66" viewBox="0 0 1200 66">
    <polygon points="0,0 620,28 0,64" fill="#dc1f41"/>
    <polygon points="0,0 1200,0 1200,3 620,28" fill="#f1f1f1"/>
  </svg>
  <div class="ghost" style="left:218px;top:2452px;font-size:96px">TESTIMONIALS</div>
  <h2 class="section-title" style="top:2516px;color:#fff">Our Testimonials</h2>
  <div class="abs testi-video" role="img" aria-label="Video still of four panelists seated on stage in front of a purple event screen">
    <div class="play-ring"></div>
    <svg class="abs" style="left:240px;top:160px" width="20" height="24" viewBox="0 0 20 24"><polygon points="3,2 18,12 3,22" fill="#fff"/></svg>
  </div>
  <div class="abs dots"><span></span><span></span><span></span><span></span></div>

  <div class="review" style="top:2593px">
    <div class="avatar" role="img" aria-label="Client headshot"></div>
    <svg class="quote" width="36" height="22" viewBox="0 0 36 22"><path d="M2 0h14v10l-6 12H4l5-10H2zM20 0h14v10l-6 12h-6l5-10h-7z" fill="#dc1f41"/></svg>
    <div class="review-body"><div class="review-name">JOHN SMITH<small>John Smith</small></div><p class="review-text">Lorem ipsum dolor sit amet, kltur adipiscing elit, sed do eiusmod tempor iidure et dolore magna aliqua.</p></div>
  </div>
  <div class="review" style="top:2733px">
    <div class="avatar" role="img" aria-label="Client headshot"></div>
    <svg class="quote" width="36" height="22" viewBox="0 0 36 22"><path d="M2 0h14v10l-6 12H4l5-10H2zM20 0h14v10l-6 12h-6l5-10h-7z" fill="#dc1f41"/></svg>
    <div class="review-body"><div class="review-name">JOHN SMITH<small>John Smith</small></div><p class="review-text">Lorem ipsum dolor sit amet, kltur adipiscing elit, sed do eiusmod tempor iidure et dolore magna aliqua.</p></div>
  </div>
  <div class="review" style="top:2873px">
    <div class="avatar" role="img" aria-label="Client headshot"></div>
    <svg class="quote" width="36" height="22" viewBox="0 0 36 22"><path d="M2 0h14v10l-6 12H4l5-10H2zM20 0h14v10l-6 12h-6l5-10h-7z" fill="#dc1f41"/></svg>
    <div class="review-body"><div class="review-name">JOHN SMITH<small>John Smith</small></div><p class="review-text">Lorem ipsum dolor sit amet, kltur adipiscing elit, sed do eiusmod tempor iidure et dolore magna aliqua.</p></div>
  </div>
  <svg class="abs" style="left:0;top:3036px" width="1200" height="56" viewBox="0 0 1200 56">
    <polygon points="600,56 1200,0 1200,56" fill="#dc1f41"/>
  </svg>

  <!-- Gallery -->
  <h2 class="section-title" style="top:3132px;color:#111">Our Gallery</h2>
  <div class="abs gallery">
    <div role="img" aria-label="Photo of the speaker with a guest at an event" style="background:linear-gradient(160deg,#8a7f74,#3d3a38)"></div>
    <div role="img" aria-label="Photo of an interview filmed in a studio" style="background:linear-gradient(160deg,#f2f2f2,#9a9ca4)"></div>
    <div role="img" aria-label="Photo of the speaker at a conference" style="background:linear-gradient(160deg,#6e5a4c,#2d2622)"></div>
    <div role="img" aria-label="Photo of the speaker with a guest at night" style="background:linear-gradient(160deg,#485766,#1f2530)"></div>
    <div role="img" aria-label="Photo of the speaker in front of a summit backdrop" style="background:linear-gradient(160deg,#d9d4cf,#5d6f8c)"></div>
    <div role="img" aria-label="Photo of the speaker with a guest indoors" style="background:linear-gradient(160deg,#b8b2a6,#4a463f)"></div>
    <div role="img" aria-label="Photo of the speaker with a guest at a venue" style="background:linear-gradient(160deg,#7a6b60,#2b2622)"></div>
    <div role="img" aria-label="Photo of the speaker with a guest in a hall" style="background:linear-gradient(160deg,#a59b8f,#3b3632)"></div>
  </div>
  <div class="btn gallery-btn">View All</div>

  <!-- Newsletter & footer -->
  <div class="abs footer-bg"></div>
  <svg class="abs" style="left:0;top:3810px" width="1200" height="70" viewBox="0 0 1200 70">
    <polygon points="0,34 1200,0 1200,12 0,70" fill="#dc1f41"/>
    <polygon points="0,70 1200,12 1200,70" fill="#1d1d1f"/>
  </svg>
  <div class="abs newsletter">
    <h2>Sign For Newsletter</h2>
    <div class="nl-input">Enter Email Here</div>
    <div class="btn nl-btn">Subscribe</div>
  </div>
  <div class="abs footer-brand">Petros Valtinos</div>
  <div class="abs socials"><span>F</span><span>T</span><span>L</span><span>I</span></div>
  <nav class="abs footer-nav"><span>HOME</span><span>ABOUT US</span><span>OUR SERVICES</span><span>TESTIMONIALS</span><span>CONTACT US</span></nav>
  <div class="abs footer-rule"></div>
  <p class="abs copyright">©Copyright 2023 Petros Valtinos. All Rights Reserved.</p>
</div>
</body>
</html>
```